Business card to promote business guidance

I need a card design to give to all my customers advertising a way to build a business exactly like the one they just bought from. I have an online store and will include one with each shipment. It should state the way to financial freedom and working for yourself

Target Market(s)

Young Entrepreneurs that want to start and don't know how

Industry/Entity Type

Business

Contact Information for Business Card

"You just bought from a successful company on Brindlemart. I have a unique business model, discovered by me, unlike any other that can make anyone successful. Follow me and message me for exactly the same model. If you ever wanted to work for yourself, I will teach you how. It's not a pipe dream, allow me to guide you out of the box."

Colors
85abd2

Requirements
Must have
• website www.dorianwelkby.example
instagram @thedorianwelkby

```html
<!DOCTYPE html>
<html lang="en">
<head>
<meta charset="utf-8">
<title>Dorian Welkby – Business Card</title>
<link href="https://fonts.googleapis.com/css2?family=Arimo:ital@1&family=PT+Sans&display=swap" rel="stylesheet">
<style>
  :root {
    --ink-blue: #0a6bbd;
    --ink-dark: #1a1a1a;
    --band-green: #27b674;
    --band-teal: #00a99d;
    --band-sky: #29abe2;
    --band-deep: #0071bc;
    --paper: #ffffff;
  }
  html, body {
    margin: 0;
    padding: 0;
    overflow: hidden;
    background: var(--paper);
  }
  .card {
    position: relative;
    width: 1200px;
    height: 686px;
    background: var(--paper);
    overflow: hidden;
  }
  .card__bands {
    position: absolute;
    inset: 0;
    width: 1200px;
    height: 686px;
  }
  .card__pitch {
    position: absolute;
    left: 0;
    width: 1200px;
    margin: 0;
    text-align: center;
    font-family: "Arimo", Arial, sans-serif;
    font-style: italic;
    font-size: 27px;
    line-height: 31.5px;
    color: var(--ink-blue);
  }
  .card__pitch--intro { top: 123px; }
  .card__pitch--offer { top: 249px; }
  .card__call {
    position: absolute;
    left: 0;
    top: 343px;
    width: 1200px;
    margin: 0;
    text-align: center;
    font-family: "Arimo", Arial, sans-serif;
    font-style: italic;
    font-size: 35px;
    line-height: 40px;
    color: var(--ink-dark);
  }
  .contact {
    position: absolute;
    top: 520px;
    display: flex;
    align-items: center;
    gap: 10px;
    font-family: "PT Sans", "Myriad Pro", sans-serif;
    font-size: 34px;
    line-height: 42px;
    color: var(--paper);
  }
  .contact--web { left: 129px; }
  .contact--social { left: 788px; }
  .contact__icon { width: 30px; height: 30px; flex: none; }
  .contact__mark {
    width: 26px;
    height: 26px;
    border: 3px solid var(--paper);
    border-radius: 6px;
    flex: none;
  }
</style>
</head>
<body>
<main class="card">
  <svg class="card__bands" viewBox="0 0 1200 686" aria-hidden="true">
    <path fill="var(--band-green)" d="M0 402 Q600 440 1200 396 L1200 408 Q600 454 0 414 Z"/>
    <path fill="var(--band-teal)" d="M0 424 Q600 462 1200 418 L1200 436 Q600 480 0 442 Z"/>
    <path fill="var(--band-sky)" d="M0 450 Q600 486 1200 444 L1200 686 L0 686 Z"/>
    <path fill="var(--band-deep)" d="M0 464 Q600 500 1200 458 L1200 686 L0 686 Z"/>
  </svg>

  <p class="card__pitch card__pitch--intro">You just bought from a successful company on Brindlemart. I have a unique<br>business model, discovered by me, unlike any other that can make anyone<br>successful.</p>
  <p class="card__pitch card__pitch--offer">If you ever wanted to work for yourself, I will teach you how. It's not a pipe<br>dream, allow me to guide you out of the box.</p>

  <p class="card__call">Follow me and message me for exactly the same model.</p>

  <div class="contact contact--web">
    <svg class="contact__icon" viewBox="0 0 30 30" aria-hidden="true" fill="none" stroke="#ffffff" stroke-width="2.2">
      <circle cx="15" cy="15" r="13"/>
      <ellipse cx="15" cy="15" rx="6" ry="13"/>
      <line x1="15" y1="2" x2="15" y2="28"/>
      <line x1="2" y1="15" x2="28" y2="15"/>
      <line x1="4.5" y1="8.5" x2="25.5" y2="8.5"/>
      <line x1="4.5" y1="21.5" x2="25.5" y2="21.5"/>
    </svg>
    <span class="contact__text">www.dorianwelkby.example</span>
  </div>

  <div class="contact contact--social">
    <span class="contact__mark" aria-hidden="true"></span>
    <span class="contact__text">@thedorianwelkby</span>
  </div>
</main>
</body>
</html>
```